Red Kettle Handcrafted Tomato Ketchup packaging design modern

From the best ingredients there is the best ketchup Red Handcrafted ketchup are specially formulated for fine dining and drinks, bringing out all the flavors. As the Red Kettle handcrafted ketchup is otherwise fabulous: Made with wholesome, fully ripe fruits Nothing with half things! All Red Kettle handcrafted ketchups are pure nature, without any artificial diluents or concentrates. Where tomato is on it, that's all there is to it - guaranteed! the design should be professional and noble despite being trendy. A watcher wants to sell the ketchup as merchandising from our restaurant. but as a single brand positioning. The ketchup is vegan. Dimensions: 6.8 cm Height: 7.8 cm Circumference: 21.6 cm The text down (Text 1-4). The lid of the text the glass packaging is black! Thanks for your efforts. I look forward to your designs.

Target Market(s)

foodies

Font styles to use
Serif
Sans Serif

Colors

Designer to choose colors to be used in the design.

Requirements
Must have
• Title: (Handcrafted Tomato Ketchup) Text One: (Store chilled after opening and consume quickly, pasteurized.) Text Two: (Handcrafted in Switzerland by Brentwick Gastro GmbH, Chur www.redkettle-example.ch) Text Tree: (Tomatoes, White Wine Vinegar, Aceto Balsamico, Brown Cane Sugar, Corn Starch, Spices, Salt) Text For: (200 grams) or (200g) The Logo of Red Kettle with the Pasta and Wine have to because of the gesety.
Nice to have
• small vegan icon (maybe)
Should not have
• text of the logo (pasta & wine)

```html
<!DOCTYPE html>
<html lang="en">
<head>
<meta charset="utf-8">
<title>Red Kettle Handcrafted Tomato Ketchup – Label</title>
<link rel="stylesheet" href="https://fonts.googleapis.com/css2?family=Josefin+Sans:wght@400&family=Oswald:wght@500&family=Dancing+Script:wght@700&display=swap">
<style>
  :root {
    --backdrop: #ececec;
    --label: #ffffff;
    --ink: #1f1f1f;
    --tomato-red: #ec1c24;
    --illustration-red: #e8574a;
    --white: #ffffff;
  }
  html, body {
    margin: 0;
    padding: 0;
    overflow: hidden;
  }
  .canvas {
    position: relative;
    width: 1200px;
    height: 1200px;
    background: var(--backdrop);
    overflow: hidden;
  }
  .label {
    position: absolute;
    left: 170px;
    top: 240px;
    width: 860px;
    height: 720px;
    background: var(--label);
  }
  .brand-name {
    position: absolute;
    left: 0;
    width: 1200px;
    top: 305px;
    margin: 0;
    text-align: center;
    font-family: "Josefin Sans", sans-serif;
    font-weight: 400;
    font-size: 44px;
    letter-spacing: 12px;
    color: var(--ink);
  }
  .accent-bar {
    position: absolute;
    left: 387px;
    top: 422px;
    width: 426px;
    height: 36px;
    background: var(--tomato-red);
  }
  .tomato-illustration {
    position: absolute;
    left: 314px;
    top: 560px;
    width: 230px;
    height: 165px;
    border-radius: 50% 45% 40% 50%;
    background: radial-gradient(ellipse at 45% 45%, #f49a8f 0%, var(--illustration-red) 70%);
    z-index: 1;
  }
  .product-title {
    position: absolute;
    right: 372px;
    top: 478px;
    margin: 0;
    text-align: right;
    font-family: "Oswald", sans-serif;
    font-weight: 500;
    color: var(--ink);
    text-transform: uppercase;
    z-index: 2;
  }
  .product-title span {
    display: block;
  }
  .title-small {
    font-size: 78px;
    line-height: 96px;
    letter-spacing: 1px;
  }
  .title-large {
    font-size: 98px;
    line-height: 106px;
    letter-spacing: 1px;
  }
  .claim-band {
    position: absolute;
    left: 387px;
    top: 851px;
    width: 426px;
    height: 36px;
    background: var(--tomato-red);
    display: flex;
    justify-content: space-between;
    align-items: center;
    padding: 0 18px 0 34px;
    box-sizing: border-box;
    font-family: "Dancing Script", cursive;
    font-weight: 700;
    font-size: 20px;
    color: var(--white);
  }
  .diet-badge {
    position: absolute;
    left: 560px;
    top: 831px;
    width: 76px;
    height: 76px;
    box-sizing: border-box;
    border-radius: 50%;
    background: var(--white);
    border: 1.5px solid var(--ink);
    z-index: 3;
  }
</style>
</head>
<body>
  <main class="canvas">
    <section class="label"></section>
    <h2 class="brand-name">RED KETTLE</h2>
    <div class="accent-bar"></div>
    <div class="tomato-illustration" role="img" aria-label="Red sketched illustration of whole and sliced tomatoes"></div>
    <h1 class="product-title">
      <span class="title-small">Handcrafted</span>
      <span class="title-large">Tomato</span>
      <span class="title-large">Ketchup</span>
    </h1>
    <div class="claim-band">
      <span>Made from</span>
      <span>fully ripe fruits</span>
    </div>
    <div class="diet-badge" role="img" aria-label="Vegan badge"></div>
  </main>
</body>
</html>
```